Layout for site fence advertising - length approx. 250 cm x 125 cm

The advertising will later be printed on a PVC film and used for events or on sports fields.

Main services :
Your regional contact at
Real estate and business financing
independent insurance advice

```html
<!DOCTYPE html>
<html lang="en">
<head>
<meta charset="utf-8">
<title>Auerbach Finanzberatung – Fence Banner</title>
<link href="https://fonts.googleapis.com/css2?family=Lexend:wght@400;500;600&display=swap" rel="stylesheet">
<style>
  :root {
    --page-bg: #f4f1f2;
    --brand-blue: #2a55a8;
    --brand-blue-deep: #1f4797;
    --ring-white: #f3f5fa;
    --text-white: #ffffff;
    --text-grey: #3e3e44;
    --sky-top: #f6f8fb;
    --sky-bottom: #dfe4ec;
    --lawn: #c6d3b6;
    --portrait-a: #5b4a3e;
    --portrait-b: #2a2c36;
  }
  * { box-sizing: border-box; margin: 0; padding: 0; }
  html, body {
    width: 1050px; height: 1200px; overflow: hidden;
    background: var(--page-bg);
    font-family: "Lexend", sans-serif;
  }
  .banner {
    position: absolute; left: 25px; top: 350px;
    width: 1000px; height: 500px; overflow: hidden;
    box-shadow: 6px 6px 14px rgba(0,0,0,0.25);
  }
  .banner__scene {
    position: absolute; inset: 0;
    background: linear-gradient(180deg, var(--sky-top) 0%, var(--sky-bottom) 78%, var(--lawn) 88%, var(--lawn) 100%);
  }
  .banner__shapes { position: absolute; inset: 0; }
  .services {
    position: absolute; left: 60px; top: 98px; width: 390px;
    color: var(--text-white); text-align: center;
    font-weight: 500; font-size: 29px; line-height: 50px;
  }
  .brand {
    position: absolute; left: 520px; top: 25px;
    display: flex; align-items: center; gap: 16px;
  }
  .brand__mark {
    width: 118px; height: 118px; border-radius: 50%;
    border: 3px solid var(--brand-blue); flex: none;
  }
  .brand__divider { width: 3px; height: 118px; background: var(--text-grey); flex: none; }
  .brand__name { color: var(--brand-blue); font-weight: 500; font-size: 22px; line-height: 1.2; }
  .brand__tagline { color: var(--text-grey); font-size: 16px; margin-top: 6px; }
  .portrait {
    position: absolute; left: 663px; top: 213px; width: 147px; height: 179px;
    border-radius: 10px 10px 0 0;
    background: linear-gradient(160deg, var(--portrait-a), var(--portrait-b));
  }
  .phone {
    position: absolute; left: 573px; top: 392px; width: 326px; height: 42px;
    background: var(--brand-blue);
    color: var(--text-white); font-weight: 600; font-size: 31px;
    line-height: 42px; text-align: center; letter-spacing: 0.5px;
  }
</style>
</head>
<body>
  <section class="banner">
    <div class="banner__scene" role="img" aria-label="Photo of a white modern two-storey house with lawn and pergola"></div>
    <svg class="banner__shapes" width="1000" height="500" viewBox="0 0 1000 500">
      <circle cx="243" cy="256" r="244" fill="var(--ring-white)" opacity="0.9"/>
      <circle cx="253" cy="241" r="232" fill="var(--brand-blue)" opacity="0.93"/>
      <path d="M 440 372 Q 455 360 462 350 L 470 378 Q 460 392 448 400 Z" fill="var(--ring-white)"/>
    </svg>
    <div class="services">
      Your regional<br>contact at<br>REAL ESTATE and<br>BUSINESS FINANCING<br>independent<br>INSURANCE advice
    </div>
    <div class="brand">
      <div class="brand__mark"></div>
      <div class="brand__divider"></div>
      <div>
        <div class="brand__name">Auerbach Finanzberatung GmbH</div>
        <div class="brand__tagline">Finanzieren, Versichern, Vorsorgen</div>
      </div>
    </div>
    <div class="portrait" role="img" aria-label="Portrait photo of the advisor in a dark suit"></div>
    <div class="phone">+43 600 245 1180</div>
  </section>
</body>
</html>
```